Awesome law firm seeks great artwork for sign to be installed at local roller skating rink!!

We're a dynamic, law firm that does its work with a difference - we actually care about our clients and our fees are usually lower than most other firms.

We are installing a sign that's 78cm (height) x 158cm (width) to be printed on 3mm Aluminum Composite Panel and installed at a local roller skating rink in Kalamunda, Perth, Western Australia.

Graphics need to be provided in vector .eps (Encapsulated Post Script), .ai (Adobe Illustrator) or PDF format.

We have uploaded a copy of our Logo, which should feature on the sign (we usually have it on the top right of our stationery, but are happy to see other suggestions), together with our practice areas - Family Law, Wills and Estates, Building and Construction, Corporate and Commercial, Local Government, General legal (personal or business).

We don't have a 'slogan' for our firm, but for the roller skating rink sign, we're thinking of something like 'We roll with you", or something similar. Surprise us :)

Sign should also indicate that our team are local to "the Hills", which is how this area (the Kalamunda and surrounding areas of Perth) is known.

Main colors of the sign can include blue, white, black and red (more blue, white and black preferred).

The final design should communicate trust and expertise in law, but have a fun edge (the sign's at a roller skating rink after all and will be seen on every lap as it's in the rink).

The sign must include our website address www.venkarilegal.com (note this is still under construction in case you google us :)), our phone number 0431 508 279 and our main email address, which is admin@venkarilegal.com

Beyond this, we're happy to see any cool ideas for the design of our sign.

Target Market(s)

Local families and business owners at local roller skating rink

Industry/Entity Type

Legal services

Font styles to use
Serif
Other font styles liked:
• Designer to choose

Colors
0054AA
0677BA
7BADD7
CADEEF
E8F1F8
EB3D1F
EC4F4E
F09395
F8D3D4
FCEDEE

Requirements
Must have
• Logo, contact details, design as per description and can have the words "Get your skates on!"
Nice to have
• Awesome, striking, appealing design - easy to read as you're zooming past on your skates!
Should not have
• Any offensive, explicit, corny or suggestive words and preferably avoid cliché rhyming catch phrases, albeit we do want something fun that has a skating vibe

```html
<!DOCTYPE html>
<html lang="en">
<head>
<meta charset="utf-8">
<title>Venkari Legal – Rink Sign</title>
<link rel="stylesheet" href="https://fonts.googleapis.com/css2?family=Montserrat:wght@500;800;900&family=Poppins:wght@600;700&family=Shrikhand&display=swap">
<style>
  :root {
    --page: #e9eaee;
    --ink: #1f1f2b;
    --navy: #14306e;
    --blue: #2d5bb5;
    --logo-blue: #4472c4;
    --outline: #3b6fd0;
    --white: #ffffff;
  }
  html, body {
    margin: 0;
    width: 1200px;
    height: 1200px;
    overflow: hidden;
    background: var(--page);
  }
  .sign {
    position: absolute;
    left: 40px;
    top: 323px;
    width: 1120px;
    height: 553px;
    background: var(--ink);
    overflow: hidden;
    box-shadow: 0 10px 30px rgba(0,0,0,.25);
  }
  .sign__shapes, .sign__portrait {
    position: absolute;
    left: 0; top: 0;
    width: 1120px; height: 553px;
  }
  .headline {
    position: absolute;
    margin: 0;
    color: var(--white);
    -webkit-text-stroke: 4px var(--outline);
    paint-order: stroke fill;
    line-height: 1;
    white-space: nowrap;
  }
  .headline--caps {
    left: 38px;
    top: 46px;
    font: 900 90px/1 "Montserrat", sans-serif;
    letter-spacing: -3px;
  }
  .headline--script {
    top: 118px;
    left: 40px;
    font: 400 98px/1 "Shrikhand", cursive;
    letter-spacing: -2px;
    transform: rotate(-3deg);
    transform-origin: left center;
  }
  .phone {
    position: absolute;
    left: 103px; top: 291px;
    width: 458px; height: 73px;
    border-radius: 12px;
    background: linear-gradient(180deg, #1b3a80 0%, #2a55b0 55%, #1b3a80 100%);
    display: flex; align-items: center;
  }
  .phone__icon {
    width: 56px; height: 56px;
    margin-left: 50px;
  }
  .phone__number {
    margin-left: 30px;
    font: 700 37px/1 "Poppins", sans-serif;
    color: var(--white);
    letter-spacing: .5px;
  }
  .practice {
    position: absolute;
    height: 21px;
    border-radius: 11px;
    background: linear-gradient(180deg, #15306c, #22469a);
    color: var(--white);
    font: 700 15.5px/21px "Poppins", sans-serif;
    text-align: center;
    white-space: nowrap;
  }
  .logo {
    position: absolute;
    left: 819px; top: 13px;
    width: 301px; height: 200px;
    background: var(--white);
    display: flex; flex-direction: column;
    justify-content: center;
    padding-left: 36px;
    box-sizing: border-box;
    color: var(--logo-blue);
    font-family: "Montserrat", sans-serif;
    font-weight: 500;
  }
  .logo__line--top { font-size: 43px; line-height: 1.1; }
  .logo__line--bottom { font-size: 66px; line-height: 1.05; }
  .footer-line {
    position: absolute;
    top: 520px;
    margin: 0;
    font: 700 16px/1 "Poppins", sans-serif;
    color: var(--ink);
    white-space: nowrap;
  }
  .website {
    left: 0; width: 1120px;
    text-align: center;
    letter-spacing: 8px;
  }
  .local-tag {
    left: 24px;
    font-size: 13px;
    top: 523px;
    color: var(--navy);
    letter-spacing: .5px;
  }
  .email {
    right: 24px;
    font-size: 13px;
    top: 523px;
    color: var(--navy);
    letter-spacing: .5px;
  }
</style>
</head>
<body>
<main class="sign">
  <svg class="sign__shapes" viewBox="0 0 1120 553" aria-hidden="true">
    <defs>
      <radialGradient id="panelGlow" cx="0.7" cy="0.5" r="0.7">
        <stop offset="0" stop-color="#3563b8"/>
        <stop offset="1" stop-color="#142b62"/>
      </radialGradient>
    </defs>
    <polygon class="panel" points="529,0 771,0 830,150 663,330" fill="url(#panelGlow)"/>
    <polygon class="slash" points="500,0 529,0 599,168" fill="#ffffff"/>
    <g class="sparkle" fill="#ffffff">
      <polygon points="424,264 600,261 615,264 600,267"/>
      <polygon points="520,238 572,237 580,238 572,239"/>
      <polygon points="520,301 590,300 599,302 590,304"/>
      <polygon points="615,232 619,258 645,264 619,270 615,296 611,270 585,264 611,258"/>
      <polygon points="580,226 582,235 590,237 582,239 580,248 578,239 570,237 578,235"/>
      <polygon points="599,290 601,299 609,302 601,305 599,314 597,305 589,302 597,299"/>
    </g>
  </svg>

  <svg class="sign__portrait" viewBox="0 0 1120 553" role="img" aria-label="Photo of a lawyer in a navy suit, arms crossed, shown from the shoulders down">
    <defs>
      <radialGradient id="suit" cx="0.45" cy="0.5" r="0.75">
        <stop offset="0" stop-color="#2a4f9e"/>
        <stop offset="1" stop-color="#172f6a"/>
      </radialGradient>
    </defs>
    <path d="M670,512 C660,440 656,330 668,262 C676,215 700,190 745,172 L800,150 L830,110 L1100,150 C1115,170 1120,200 1120,240 L1120,512 Z" fill="url(#suit)"/>
  </svg>

  <svg class="sign__shapes" viewBox="0 0 1120 553" aria-hidden="true">
    <path class="torn-edge" fill="#ffffff"
      d="M0,515 L20,508 L45,514 L70,506 L100,512 L130,505 L170,513 L200,507 L240,513 L280,506 L320,511 L360,504 L400,510 L420,500 L460,498 L500,503 L540,497 L580,502 L620,496 L660,501 L700,495 L740,500 L780,494 L820,499 L860,493 L900,498 L940,492 L980,497 L1020,491 L1060,496 L1100,490 L1120,494 L1120,553 L0,553 Z"/>
  </svg>

  <h1 class="headline headline--caps">GET YOUR</h1>
  <p class="headline headline--script">skates on!</p>

  <div class="phone">
    <svg class="phone__icon" viewBox="0 0 56 56" aria-hidden="true">
      <circle cx="28" cy="28" r="28" fill="#ffffff"/>
      <path d="M20 14 q-4 2 -4 7 q1 10 9 18 q8 8 17 9 q5 0 7 -4 l-6 -6 q-2 -1 -4 1 l-2 2 q-5 -2 -10 -8 q-4 -5 -5 -9 l2 -2 q2 -2 1 -4 z" fill="#1f1f2b"/>
    </svg>
    <span class="phone__number">0431 508 279</span>
  </div>

  <span class="practice" style="left:24px;top:401px;width:129px">FAMILY LAW</span>
  <span class="practice" style="left:173px;top:401px;width:173px">WILLS AND ESTATES</span>
  <span class="practice" style="left:366px;top:401px;width:262px">BUILDING AND CONSTRUCTION</span>
  <span class="practice" style="left:81px;top:431px;width:279px">CORPORATE AND COMMERCIAL</span>
  <span class="practice" style="left:392px;top:431px;width:193px">LOCAL GOVERNMENT</span>
  <span class="practice" style="left:147px;top:460px;width:372px">GENERAL LEGAL (PERSONAL OR BUSINESS)</span>

  <div class="logo">
    <span class="logo__line logo__line--top">VENKARI</span>
    <span class="logo__line logo__line--bottom">LEGAL</span>
  </div>

  <p class="footer-line local-tag">Your local team in the Hills</p>
  <p class="footer-line website">www.venkarilegal.com</p>
  <p class="footer-line email">admin@venkarilegal.com</p>
</main>
</body>
</html>
```